Tallow Creek Biologics - Business Card Design

Business Card Brief;
We require a design for a business card template for our business “Tallow Creek Biologics”.
We are a firm that manufacture positive microbial formulations to enhance agricultural legume crops such as lucence, soy beans and faba beans. We also manufacture microbial formulations that aid in composting of waste organic waste to use as a natural fertilizer.
We are seeking a business card design that portrays a clean, professional organisation dedicated to enhancing nature and sustainable farming techniques.
Our website is www.farobiotix.com.au
Here is a link to a drawing of a soybean plant. One of our main products is used to help grow these. I offer it an an example of the type of graphic that might be used on the card, but will leave you to create your own design; https://pictavault.example/482913067/stock-illustration-leafy-sprout-on-a-plain.html
Two cards are required;
--------------------------------------------------------------------
Card #1
Owen T Radley
Executive Chairman
Mobile: 0412 558304
Email: owen@farobiotix.com.au
---------------------------------------------------------------------------
Card #2
Felix R Dunmore
Chief Financial & Operating Officer
Mobile: 0455 284679
Email felix@farobiotix.com.au

Many thanks
Felix Dunmore

Industry/Entity Type

Agriculture

Colors

Designer to choose colors to be used in the design.

Requirements
Must have
• An elegant design that demonstrates our commitment to enhancing nature.

```html
<!DOCTYPE html>
<html lang="en">
<head>
<meta charset="utf-8">
<title>Tallow Creek Biologics – Business Cards</title>
<link href="https://fonts.googleapis.com/css2?family=Roboto:wght@400;500;700&display=swap" rel="stylesheet">
<style>
  :root {
    --backdrop: #2e2e2e;
    --card-white: #ffffff;
    --ink: #1c1c1c;
    --green-dark: #0f8a3a;
    --green-mid: #2fb34f;
    --green-light: #7fcf8a;
    --green-pale: #cfeccf;
    --sky: #e9eef0;
    --leaf: #5e9a3c;
    --soil: #8a7a66;
  }
  * { margin: 0; padding: 0; box-sizing: border-box; }
  html, body {
    width: 1200px; height: 2276px; overflow: hidden;
    background: var(--backdrop);
    font-family: "Roboto", Arial, sans-serif;
  }
  .canvas { position: relative; width: 1200px; height: 2276px; }
  .card-label {
    position: absolute; left: 0; width: 1200px;
    text-align: center; color: #fff;
    font-weight: 700; font-size: 48px; letter-spacing: 1px;
  }
  .card {
    position: absolute; left: 0; width: 1200px; height: 680px;
    background: var(--card-white); overflow: hidden;
  }
  .card svg.card-art { position: absolute; inset: 0; }
  .contact-block {
    position: absolute; right: 60px; top: 70px; text-align: right; color: var(--ink);
  }
  .person-name { font-weight: 500; font-size: 50px; line-height: 1.1; }
  .person-title { font-size: 27px; margin-top: 6px; }
  .contact-lines { margin-top: 96px; }
  .contact-line {
    display: flex; justify-content: flex-end; align-items: center;
    font-size: 27px; height: 60px; gap: 14px;
  }
  .contact-badge {
    width: 34px; height: 34px; background: var(--green-mid); color: #fff;
    font-size: 22px; font-weight: 700; display: flex; align-items: center; justify-content: center;
  }
</style>
</head>
<body>
<div class="canvas">

  <div class="card-label" style="top:140px;">CARD-#1</div>
  <section class="card" style="top:360px;">
    <svg class="card-art" width="1200" height="680" viewBox="0 0 1200 680">
      <defs>
        <linearGradient id="field1" x1="0" y1="0" x2="0" y2="1">
          <stop offset="0" stop-color="var(--sky)"/>
          <stop offset="0.3" stop-color="var(--leaf)"/>
          <stop offset="0.8" stop-color="#4f8a33"/>
          <stop offset="1" stop-color="var(--soil)"/>
        </linearGradient>
        <linearGradient id="pattern1" x1="0" y1="0" x2="1" y2="0">
          <stop offset="0" stop-color="var(--green-pale)" stop-opacity="0"/>
          <stop offset="1" stop-color="var(--green-light)" stop-opacity="0.8"/>
        </linearGradient>
      </defs>
      <rect x="760" y="0" width="440" height="680" fill="url(#pattern1)" role="img" aria-label="Faint green diamond pattern"/>
      <polygon points="0,0 340,0 600,340 340,680 0,680" fill="url(#field1)" role="img" aria-label="Photo of young soybean plants in a field"/>
      <polygon points="340,0 372,0 632,340 372,680 340,680 600,340" fill="var(--green-dark)"/>
      <polygon points="372,0 392,0 652,340 392,680 372,680 632,340" fill="var(--green-mid)"/>
    </svg>
    <div class="contact-block">
      <div class="person-name">Owen T Radley</div>
      <div class="person-title">Executive Chairman</div>
      <div class="contact-lines">
        <div class="contact-line"><span>0412 558304</span><span class="contact-badge">P</span></div>
        <div class="contact-line"><span>owen@farobiotix.com.au</span><span class="contact-badge">E</span></div>
      </div>
    </div>
  </section>

  <div class="card-label" style="top:1164px;">CARD-#2</div>
  <section class="card" style="top:1368px;">
    <svg class="card-art" width="1200" height="680" viewBox="0 0 1200 680">
      <defs>
        <linearGradient id="field2" x1="0" y1="0" x2="0" y2="1">
          <stop offset="0" stop-color="var(--sky)"/>
          <stop offset="0.3" stop-color="var(--leaf)"/>
          <stop offset="0.8" stop-color="#4f8a33"/>
          <stop offset="1" stop-color="var(--soil)"/>
        </linearGradient>
        <linearGradient id="pattern2" x1="0" y1="0" x2="1" y2="0">
          <stop offset="0" stop-color="var(--green-pale)" stop-opacity="0"/>
          <stop offset="1" stop-color="var(--green-light)" stop-opacity="0.8"/>
        </linearGradient>
      </defs>
      <rect x="760" y="0" width="440" height="680" fill="url(#pattern2)" role="img" aria-label="Faint green diamond pattern"/>
      <polygon points="0,0 340,0 600,340 340,680 0,680" fill="url(#field2)" role="img" aria-label="Photo of young soybean plants in a field"/>
      <polygon points="340,0 372,0 632,340 372,680 340,680 600,340" fill="var(--green-dark)"/>
      <polygon points="372,0 392,0 652,340 392,680 372,680 632,340" fill="var(--green-mid)"/>
    </svg>
    <div class="contact-block">
      <div class="person-name">Felix R Dunmore</div>
      <div class="person-title">Chief Financial &amp; Operating Officer</div>
      <div class="contact-lines">
        <div class="contact-line"><span>0455 284679</span><span class="contact-badge">P</span></div>
        <div class="contact-line"><span>felix@farobiotix.com.au</span><span class="contact-badge">E</span></div>
      </div>
    </div>
  </section>

</div>
</body>
</html>
```